Exec Conference Design Concept

We need to refresh & update nonprofit association graphic design for annual meeting. The graphics will be used to promote the event primarily through digital communications & social media. Other materials we generate for this event are the agenda & billboard content. You can view the existing design at www.lumivarguild.org under Events.

The target audience is primarily male, ages 35-60 in executive positions in C-Corps. The conference topics center on manufacturing regulations, marketing trends, and the economy. This conference has been around almost 30 years so we need something to invigorate potential registrants that will get their attention. It still needs to be professional and business-like.

In addition to a new design concept we would like to update the color palette. We’ve attached some mood boards with potential color & font suggestions. Our company logo is also attached and is the only design element tied to our branding that cannot be changed.

Designs should be energetic and sophisticated. Ideally, we would like the designs in Adobe Indesign or Photoshop. However, we can work with Illustrator.

Target Market(s)

Male business executives age 35-60.

Industry/Entity Type

Polystyrene manufacturing industry supply chain.

Font styles to use
Other font styles liked:
• I usually prefer sans serif

Requirements
Must have
• Focus points to draw attention to higher level informational units. For example, some people will only read the headers and not detailed copy.
Nice to have
• Ways to insert bonus content that don’t over power other content. I like to see a good use of white space to enhance readability.

```html
<!DOCTYPE html>
<html lang="en">
<head>
<meta charset="utf-8">
<title>Lumivar Summit 2026 – Invitation Concept</title>
<link rel="stylesheet" href="https://fonts.googleapis.com/css2?family=Montserrat:wght@400;500;700&family=Playfair+Display:wght@400;500&display=swap">
<style>
  :root {
    --white: #ffffff;
    --sage-light: #a6afa8;
    --sage: #7f8c86;
    --brown: #583728;
    --panel: #e4e4e4;
    --ink: #111111;
    --frame-green: #7a8a6a;
    --serif: "Playfair Display", Georgia, serif;
    --sans: "Montserrat", Arial, sans-serif;
  }
  * { box-sizing: border-box; margin: 0; padding: 0; }
  html, body { width: 1200px; height: 1200px; overflow: hidden; background: var(--white); }
  .canvas { position: relative; width: 1200px; height: 1200px; font-family: var(--sans); color: var(--ink); }

  .brand-tile {
    position: absolute; background: var(--sage);
    border-radius: 0 44px 0 44px;
    display: flex; flex-direction: column; justify-content: center; padding: 0 16px;
  }
  .brand-tile .brand-name { font-family: var(--sans); font-weight: 700; color: var(--white); line-height: 1.05; }
  .brand-tile .brand-url { font-family: var(--sans); color: var(--sage-light); margin-top: 8px; }
  .brand-tile--large { left: 60px; top: 165px; width: 225px; height: 198px; }
  .brand-tile--large .brand-name { font-size: 38px; }
  .brand-tile--large .brand-url { font-size: 12px; }
  .brand-tile--small { left: 367px; top: 165px; width: 79px; height: 68px; border-radius: 0 14px 0 14px; padding: 0 7px; z-index: 2; }
  .brand-tile--small .brand-name { font-size: 13px; }
  .brand-tile--small .brand-url { font-size: 4px; margin-top: 3px; }
  .brand-tile--hero { left: 839px; top: 264px; width: 112px; height: 99px; border-radius: 0 0 0 22px; padding: 0 9px; z-index: 2; }
  .brand-tile--hero .brand-name { font-size: 19px; }
  .brand-tile--hero .brand-url { font-size: 6px; margin-top: 5px; }

  .invite-panel { position: absolute; left: 342px; top: 158px; width: 750px; height: 859px; background: var(--panel); }

  .hero {
    position: absolute; left: 342px; top: 197px; width: 750px; height: 211px;
    background:
      radial-gradient(ellipse at 85% 30%, rgba(110,125,95,0.75), rgba(110,125,95,0) 55%),
      linear-gradient(100deg, #b5b3a4 0%, #dcdad0 30%, #ecebe5 60%, #d6d4c8 100%);
    border-bottom: 3px solid #000;
  }
  .hero-welcome { position: absolute; left: 447px; top: 228px; font-family: var(--serif); font-size: 28px; font-weight: 400; z-index: 2; }
  .hero-rule { position: absolute; left: 447px; top: 268px; width: 47px; height: 1px; background: var(--white); z-index: 2; }
  .hero-title { position: absolute; left: 446px; top: 272px; font-family: var(--serif); font-size: 39px; font-weight: 500; color: var(--brown); letter-spacing: -0.5px; z-index: 2; }
  .hero-tagline { position: absolute; left: 449px; top: 330px; font-size: 11.6px; font-weight: 500; line-height: 14px; z-index: 2; }
  .hero-cta { position: absolute; left: 446px; top: 370px; width: 92px; height: 17px; background: #5c6660; color: var(--white); font-size: 7.5px; display: flex; align-items: center; justify-content: center; letter-spacing: 0.3px; z-index: 2; }

  .invite-heading { position: absolute; left: 398px; top: 510px; font-family: var(--serif); font-size: 38px; font-weight: 400; letter-spacing: -0.5px; }
  .invite-subhead { position: absolute; left: 398px; top: 626px; font-size: 16px; line-height: 22px; font-weight: 400; }
  .invite-body { position: absolute; left: 398px; top: 691px; width: 290px; font-size: 12.4px; line-height: 18.3px; }

  .venue-photo {
    position: absolute; left: 718px; top: 482px; width: 304px; height: 318px;
    border: 4px solid var(--frame-green); border-radius: 0 48px 0 48px;
    background: linear-gradient(115deg, #c9c2b2 0%, #e6e1d4 45%, #f4f1ea 60%, #d8d2c4 100%);
  }

  .cta-button { position: absolute; left: 398px; top: 890px; width: 218px; height: 44px; background: var(--sage); color: var(--white); font-size: 19px; letter-spacing: 0.5px; display: flex; align-items: center; justify-content: center; }

  .palette { position: absolute; left: 717px; top: 853px; display: flex; gap: 14px; }
  .swatch { width: 66px; text-align: center; }
  .swatch-dot { width: 66px; height: 66px; border-radius: 50%; }
  .swatch-code { margin-top: 12px; font-size: 10px; }
  .swatch--white .swatch-dot { background: var(--white); }
  .swatch--sage-light .swatch-dot { background: var(--sage-light); }
  .swatch--sage .swatch-dot { background: var(--sage); }
  .swatch--brown .swatch-dot { background: var(--brown); }
</style>
</head>
<body>
<div class="canvas">
  <div class="brand-tile brand-tile--large">
    <div class="brand-name">Lumivar Summit</div>
    <div class="brand-url">www.lumivarguild.org</div>
  </div>

  <div class="invite-panel"></div>

  <div class="hero" role="img" aria-label="Soft textured stone backdrop with faint palm fronds in sage green"></div>
  <div class="brand-tile brand-tile--small">
    <div class="brand-name">Lumivar Summit</div>
    <div class="brand-url">www.lumivarguild.org</div>
  </div>
  <h2 class="hero-welcome">Welcome to the</h2>
  <div class="hero-rule"></div>
  <h1 class="hero-title">Lumivar Summit 2026</h1>
  <p class="hero-tagline">The Leading Conference on Regulatory, Communications<br>&amp; Economics for the Manufacturing Industry</p>
  <div class="hero-cta">LEARN MORE</div>
  <div class="brand-tile brand-tile--hero">
    <div class="brand-name">Lumivar Summit</div>
    <div class="brand-url">www.lumivarguild.org</div>
  </div>

  <h2 class="invite-heading">You're Invited!</h2>
  <p class="invite-subhead">Join Us at the Premiere Event for<br>Manufacturing Professionals</p>
  <p class="invite-body">Lorem ipsum dolor sit amet, consectetuer adipiscing elit. Malenelpse, comnsm per innunsido elit. Dens unlesqua NFOMA por d enit perise, atrices ned quis nehuscliq!.</p>

  <div class="venue-photo" role="img" aria-label="Sunlit cracked concrete wall with leaf shadows and a green plant at the corner"></div>

  <div class="cta-button">LEARN MORE</div>

  <div class="palette">
    <div class="swatch swatch--white"><div class="swatch-dot"></div><div class="swatch-code">#ffffff</div></div>
    <div class="swatch swatch--sage-light"><div class="swatch-dot"></div><div class="swatch-code">#a6afa8</div></div>
    <div class="swatch swatch--sage"><div class="swatch-dot"></div><div class="swatch-code">#7f8c86</div></div>
    <div class="swatch swatch--brown"><div class="swatch-dot"></div><div class="swatch-code">#583728</div></div>
  </div>
</div>
</body>
</html>
```